Bramblecrest Access & Mobility Elder Ledger

We need an ad to run in various publications that highlights our products & services. Wheelchairs, Accessible Vans, Walkers, Scooters, Home Access & Auto access

```html
<!DOCTYPE html>
<html lang="en">
<head>
<meta charset="utf-8">
<title>Bramblecrest Access &amp; Mobility – Rental Ad</title>
<link href="https://fonts.googleapis.com/css2?family=Jost:wght@700&family=Poppins:wght@500;600;700&display=swap" rel="stylesheet">
<style>
  :root {
    --brown: #7b3f1e;
    --mauve: #9a8c9b;
    --navy: #272654;
    --white: #ffffff;
    --photo-warm: #c9a27c;
    --photo-light: #efe2cf;
    --photo-wood: #8a4a26;
    --product-tone: #e6e4ea;
  }
  * { margin: 0; padding: 0; box-sizing: border-box; }
  html, body { width: 1200px; height: 1200px; overflow: hidden; background: var(--white); }
  .ad { position: relative; width: 1200px; height: 1200px; background: var(--white); font-family: "Poppins", sans-serif; }

  .brand { position: absolute; left: 0; top: 0; width: 648px; height: 172px; display: flex; align-items: center; justify-content: center; gap: 14px; }
  .brand-mark { width: 22px; height: 22px; background: var(--navy); }
  .brand-name { color: var(--navy); font-weight: 700; font-size: 30px; line-height: 1.1; letter-spacing: 0.5px; }

  .hero-photo { position: absolute; left: 648px; top: 0; width: 552px; height: 766px;
    background: linear-gradient(180deg, var(--photo-light) 0%, var(--photo-warm) 55%, var(--photo-wood) 100%); }

  .headline-panel { position: absolute; left: 0; top: 172px; width: 685px; height: 349px; background: var(--brown); padding: 70px 0 0 60px; }
  .headline { font-family: "Jost", sans-serif; font-weight: 700; color: var(--white); font-size: 62px; line-height: 70px; letter-spacing: 0.5px; }

  .intro-panel { position: absolute; left: 0; top: 521px; width: 685px; height: 245px; background: var(--mauve); padding: 12px 0 0 60px; }
  .intro { color: var(--white); font-weight: 500; font-size: 27px; line-height: 42px; }

  .products { position: absolute; left: 0; top: 766px; width: 1200px; height: 191px; background: var(--white); }
  .product { position: absolute; top: 12px; width: 150px; height: 166px; border-radius: 10px;
    background: radial-gradient(circle at 50% 50%, #cfccd6 0%, var(--product-tone) 60%, var(--white) 100%); }
  .product.walker { left: 120px; }
  .product.power-chair { left: 395px; }
  .product.scooter { left 0; left: 660px; }
  .product.lift-chair { left: 975px; }

  .offer-panel { position: absolute; left: 0; top: 957px; width: 614px; height: 243px; background: var(--navy); padding: 18px 0 0 59px; }
  .offer { color: var(--white); font-weight: 500; font-size: 34px; line-height: 49px; }

  .cta-panel { position: absolute; left: 614px; top: 957px; width: 586px; height: 243px; background: var(--mauve); padding: 34px 0 0 47px; color: var(--navy); }
  .cta-label { font-weight: 700; font-size: 20px; letter-spacing: 2px; }
  .cta-line { font-weight: 600; font-size: 40px; letter-spacing: 3px; line-height: 1.2; margin-top: 2px; }
  .cta-phone { font-weight: 700; font-size: 58px; letter-spacing: 5px; line-height: 1.1; margin-left: -8px; }
</style>
</head>
<body>
<main class="ad">
  <header class="brand">
    <span class="brand-mark"></span>
    <span class="brand-name">Bramblecrest<br>Access &amp; Mobility</span>
  </header>

  <div class="hero-photo" role="img" aria-label="Photo of a senior woman seated on a stair lift and a senior man standing on a carpeted staircase in a warm home interior"></div>

  <section class="headline-panel">
    <h1 class="headline">ACCESS &amp; MOBILITY<br>FOR ALL AREAS<br>OF YOUR LIFE</h1>
  </section>

  <section class="intro-panel">
    <p class="intro">Don’t let your clients miss out on family<br>vacations because of mobility issues.<br>Rent a wheelchair<br>accessible van for local<br>&nbsp;or long distance travel.</p>
  </section>

  <section class="products">
    <div class="product walker" role="img" aria-label="Rolling walker with seat"></div>
    <div class="product power-chair" role="img" aria-label="Power wheelchair"></div>
    <div class="product scooter" role="img" aria-label="Red mobility scooter with basket"></div>
    <div class="product lift-chair" role="img" aria-label="Blue lift recliner chair"></div>
  </section>

  <section class="offer-panel">
    <p class="offer">get 50 free miles on your<br>rental.&nbsp; Rental reservations<br>are filling up, so<br>don’t delay!</p>
  </section>

  <section class="cta-panel">
    <p class="cta-label">Call today:</p>
    <p class="cta-line">Get Yours Reserved.</p>
    <p class="cta-phone">970-555-0148</p>
  </section>
</main>
</body>
</html>
```